Business card design for engineering firm specializing in defense industry.

We need a professional business card design. Something simple but stands out. We are an engineering company specializing in composites in the defense industry.
Industry/Entity Type
Defense
Contact Information for Business Card
A simple black business card with the Varlonix yellow color is what we had in mind but open for other designs.
Colors
ffc214

```html
<!DOCTYPE html>
<html lang="en">
<head>
<meta charset="utf-8">
<title>Varlonix Business Card</title>
<link rel="stylesheet" href="https://fonts.googleapis.com/css2?family=Oswald:wght@500;600&family=Roboto:wght@400&display=swap">
<style>
  :root {
    --page: #e4e4e2;
    --card-dark: #0b0b0b;
    --card-mid: #222222;
    --brand-yellow: #ffc214;
    --ink-white: #f4f4f4;
    --ink-soft: #d8d8d8;
  }
  * { box-sizing: border-box; margin: 0; padding: 0; }
  html, body { width: 1200px; height: 1023px; overflow: hidden; }
  body {
    background: var(--page);
    position: relative;
    font-family: "Roboto", Arial, sans-serif;
  }
  .card {
    position: absolute;
    left: 250px;
    width: 700px;
    height: 400px;
    border-radius: 6px;
    background: linear-gradient(115deg, var(--card-dark) 0%, var(--card-mid) 48%, var(--card-dark) 100%);
    box-shadow: 0 10px 24px rgba(0,0,0,0.25);
    overflow: hidden;
  }
  .card--front { top: 60px; }
  .card--back { top: 563px; }

  .brand {
    position: absolute;
    display: flex;
    align-items: center;
    gap: 14px;
  }
  .brand__mark {
    width: 30px;
    height: 30px;
    background: var(--brand-yellow);
  }
  .brand__name {
    font-family: "Oswald", Arial, sans-serif;
    font-weight: 600;
    font-size: 58px;
    letter-spacing: 1px;
    color: var(--ink-white);
    line-height: 1;
  }
  .card--front .brand { left: 50%; top: 50%; transform: translate(-50%, -50%); }
  .card--back .brand { left: 95px; top: 255px; }
  .card--back .brand__name { font-size: 50px; }

  .edge-bar {
    position: absolute;
    width: 10px;
    top: 26px;
    bottom: 26px;
    border-radius: 5px;
    background: var(--brand-yellow);
    box-shadow: 0 0 14px rgba(255,194,20,0.6);
  }
  .edge-bar--left { left: 12px; }
  .edge-bar--right { right: 12px; }

  .identity {
    position: absolute;
    right: 70px;
    top: 42px;
    text-align: right;
    font-family: "Oswald", Arial, sans-serif;
    line-height: 1;
  }
  .identity__name {
    font-weight: 600;
    font-size: 40px;
    color: var(--ink-white);
    letter-spacing: 0.5px;
  }
  .identity__title {
    margin-top: 6px;
    font-weight: 500;
    font-size: 24px;
    color: var(--brand-yellow);
  }

  .contacts {
    position: absolute;
    right: 70px;
    top: 130px;
    width: 300px;
    list-style: none;
  }
  .contacts__item {
    position: relative;
    text-align: right;
    font-size: 17px;
    color: var(--ink-soft);
    height: 48px;
    padding-top: 8px;
  }
  .contacts__rule {
    position: absolute;
    left: 0;
    bottom: 6px;
    width: 300px;
    height: 34px;
    overflow: visible;
  }
</style>
</head>
<body>
  <section class="card card--front" aria-label="Card front">
    <div class="brand">
      <span class="brand__mark"></span>
      <span class="brand__name">Varlonix</span>
    </div>
  </section>

  <section class="card card--back" aria-label="Card back">
    <span class="edge-bar edge-bar--left"></span>
    <span class="edge-bar edge-bar--right"></span>

    <div class="identity">
      <p class="identity__name">DANIEL REEVE</p>
      <p class="identity__title">BUSINESS TITLE</p>
    </div>

    <ul class="contacts">
      <li class="contacts__item">555-014-2290
        <svg class="contacts__rule" viewBox="0 0 300 34"><polyline points="300,2 30,2 12,32" fill="none" stroke="#ffc214" stroke-width="2"/></svg>
      </li>
      <li class="contacts__item">www.varlonixinc.com
        <svg class="contacts__rule" viewBox="0 0 300 34"><polyline points="300,2 30,2 12,32" fill="none" stroke="#ffc214" stroke-width="2"/></svg>
      </li>
      <li class="contacts__item">email@varlonixinc.com</li>
    </ul>

    <div class="brand">
      <span class="brand__mark"></span>
      <span class="brand__name">Varlonix</span>
    </div>
  </section>
</body>
</html>
```